OUTRAGEOUS NEW Website Coral Cove Massage

Need an OUTRAGEOUSLY BOLD, Brand New Website for a National Massage Chain with a Palm Beach Tropical Theme. Graphics/Fonts/Colors/Backgrounds should be EXTREMELY, EXTREMELY Bold, Attractive and Inviting. Not looking for same-old/same-old but a website that is memorable and vivid. Standard website designs will be rejected.
Creative, technically superior, artistic Web Designers with a GREAT eye feel free to compete and GIVE us your BEST!!!

Target Market(s)

Everyone

Industry/Entity Type

Massage

Number of Pages Required

5+ page

Requirements
Must have
• BIG, BOLD, BRIGHT COLORS/GRAPHICS/FONTS
Nice to have
• Name/Email address Lead Generation Box above the fold

```html
<!DOCTYPE html>
<html lang="en">
<head>
<meta charset="utf-8">
<title>Coral Cove Massage</title>
<link rel="stylesheet" href="https://fonts.googleapis.com/css2?family=Anton&family=Open+Sans:wght@300;400;600;700&family=Space+Mono:ital@0;1&display=swap">
<style>
  :root {
    --white: #ffffff;
    --mint: #12f57c;
    --aqua: #00f2c6;
    --magenta: #f20ae6;
    --ink: #222222;
    --footer-ink: #333333;
    --brand-blue: #1f4fb5;
    --sky: #2fc3f2;
    --jungle: #2fd12a;
    --sand: #e9f3e0;
    --sea: #3fd9d4;
  }
  html, body { margin: 0; padding: 0; overflow: hidden; background: var(--white); }
  .canvas {
    position: relative;
    width: 776px;
    height: 1200px;
    overflow: hidden;
    background: var(--white);
    font-family: "Open Sans", Arial, sans-serif;
  }
  .hero-scene {
    position: absolute; left: 0; top: 0; width: 776px; height: 470px;
    background:
      radial-gradient(ellipse 260px 230px at 90px 110px, var(--jungle), rgba(47,209,42,0) 100%),
      radial-gradient(ellipse 200px 90px at 600px 215px, #2aa83a, rgba(42,168,58,0) 100%),
      radial-gradient(ellipse 330px 160px at 220px 380px, var(--sand), rgba(233,243,224,0) 100%),
      radial-gradient(ellipse 300px 130px at 640px 330px, var(--sea), rgba(63,217,212,0) 100%),
      linear-gradient(180deg, var(--sky) 0%, #6cd9ee 55%, #b9ecd8 100%);
  }
  .backdrop { position: absolute; left: 0; top: 0; }
  .massage-scene {
    position: absolute; left: 0; top: 850px; width: 452px; height: 220px;
    clip-path: polygon(0 2px, 436px 12px, 450px 218px, 0 218px);
    background:
      radial-gradient(ellipse 160px 90px at 330px 150px, #f3a6d8, rgba(243,166,216,0) 100%),
      linear-gradient(135deg, #e98ab0 0%, #f0a0c8 45%, #d98ae0 100%);
  }
  .stones-scene {
    position: absolute; left: 52px; top: 478px; width: 234px; height: 104px;
    border-radius: 50px;
    background: radial-gradient(ellipse 110px 48px at 150px 52px, #2b2b2b, rgba(43,43,43,0.15) 90%, rgba(255,255,255,0) 100%);
  }
  .brand-name {
    position: absolute; left: 0; width: 776px; top: 56px;
    text-align: center; color: var(--white);
    font-weight: 700; font-size: 21px; letter-spacing: 0.5px;
  }
  .headline {
    position: absolute; left: 302px; top: 148px;
    font-family: "Anton", Impact, sans-serif; color: var(--white);
    text-transform: uppercase; line-height: 34px; font-size: 37px; margin: 0; font-weight: 400;
  }
  .headline .big { display: block; font-size: 72px; line-height: 70px; letter-spacing: 1px; }
  .slider-arrow { position: absolute; top: 220px; }
  .slider-arrow.prev { left: 18px; }
  .slider-arrow.next { left: 744px; }
  .main-nav { position: absolute; top: 402px; left: 0; width: 776px; }
  .main-nav a {
    position: absolute; color: var(--white); text-decoration: none;
    font-size: 14px; font-weight: 300; white-space: nowrap;
  }
  .main-nav a.active { font-weight: 600; }
  .intro-kicker {
    position: absolute; right: 42px; top: 484px; text-align: right;
    color: var(--white); font-weight: 300; font-size: 13px; line-height: 15px;
  }
  .intro-kicker strong { font-weight: 700; font-size: 19px; }
  .intro-title {
    position: absolute; right: 32px; top: 518px; margin: 0;
    color: var(--white); font-weight: 300; font-size: 64px; line-height: 64px; letter-spacing: 1px;
  }
  .promise-list { position: absolute; left: 34px; top: 644px; margin: 0; padding: 0; list-style: none; }
  .promise-list li {
    font-family: "Space Mono", monospace; font-style: italic; color: var(--white);
    font-size: 33px; line-height: 40px; letter-spacing: 2px;
    border-bottom: 2px solid var(--white); display: table; padding: 0 0 0 4px; margin-bottom: 26px;
  }
  .promise-copy {
    position: absolute; right: 22px; top: 654px; margin: 0; text-align: right;
    font-family: "Space Mono", monospace; font-variant: small-caps; color: var(--white);
    font-size: 10px; line-height: 15.7px; letter-spacing: 0.4px;
  }
  .outline-button {
    position: absolute; border: 2px solid var(--white); color: var(--white);
    font-family: "Space Mono", monospace; text-transform: uppercase; letter-spacing: 2px;
    display: flex; align-items: center; justify-content: center; box-sizing: border-box;
    text-decoration: none;
  }
  .read-more { left: 645px; top: 851px; width: 111px; height: 31px; font-size: 14px; }
  .discover { left: 153px; top: 975px; width: 117px; height: 43px; font-size: 14px; }
  .feature-title {
    position: absolute; left: 0; width: 432px; top: 932px; text-align: center;
    color: var(--white); font-weight: 400; font-size: 17px; margin: 0;
  }
  .offer-title {
    position: absolute; left: 450px; width: 334px; top: 924px; text-align: center; margin: 0;
    font-family: "Space Mono", monospace; color: var(--white); font-weight: 400;
    font-size: 18px; letter-spacing: 2px;
  }
  .offer-copy {
    position: absolute; left: 450px; width: 334px; top: 970px; text-align: center; margin: 0;
    font-family: "Space Mono", monospace; font-variant: small-caps; color: var(--white);
    font-size: 10px; line-height: 15.7px; letter-spacing: 0.4px;
  }
  .footer-brand {
    position: absolute; left: 22px; top: 1086px; width: 80px;
    color: var(--brand-blue); font-weight: 700; font-size: 13px; line-height: 14px;
  }
  .footer-col { position: absolute; top: 1093px; color: var(--footer-ink); font-size: 7.5px; }
  .footer-col h4 { margin: 0 0 17px 0; font-weight: 400; font-size: 7.5px; }
  .footer-col p { margin: 0 0 6px 0; line-height: 10px; }
  .social { position: absolute; top: 1094px; }
  .social span {
    position: absolute; width: 30px; height: 30px; border-radius: 50%; background: var(--ink);
  }
</style>
</head>
<body>
<div class="canvas">
  <div class="hero-scene" role="img" aria-label="Tropical beach with palm trees, white sand and turquoise sea"></div>

  <svg class="backdrop" width="776" height="1200" viewBox="0 0 970 1500" preserveAspectRatio="none" aria-hidden="true">
    <polygon points="0,575 970,520 970,800 0,740" fill="var(--white)"/>
    <polygon points="540,548 970,520 970,800 335,772" fill="var(--mint)"/>
    <polygon points="0,730 335,770 970,790 970,1145 545,1078 0,1065" fill="var(--aqua)"/>
    <polygon points="545,1076 970,1140 970,1335 563,1335" fill="var(--magenta)"/>
    <rect x="0" y="1335" width="970" height="165" fill="var(--white)"/>
    <line x1="0" y1="1335.5" x2="970" y2="1335.5" stroke="#9a9a9a" stroke-width="1"/>
  </svg>

  <div class="stones-scene" role="img" aria-label="Stack of black hot stones with a bamboo leaf"></div>
  <div class="massage-scene" role="img" aria-label="Woman relaxing while receiving a back massage"></div>

  <header>
    <div class="brand-name">Coral Cove Massage</div>
    <h1 class="headline">Everything<br>You need to<br>Know about<span class="big">Relax</span></h1>
    <svg class="slider-arrow prev" width="16" height="26" viewBox="0 0 16 26" aria-hidden="true"><polyline points="13,2 3,13 13,24" fill="none" stroke="#fff" stroke-width="1.5"/></svg>
    <svg class="slider-arrow next" width="16" height="26" viewBox="0 0 16 26" aria-hidden="true"><polyline points="3,2 13,13 3,24" fill="none" stroke="#fff" stroke-width="1.5"/></svg>
    <nav class="main-nav">
      <a class="active" href="#" style="left:177px">COMPANY</a>
      <a href="#" style="left:306px">WORK</a>
      <a href="#" style="left:401px">CONTACTS</a>
      <a href="#" style="left:521px">SIGN IN</a>
    </nav>
  </header>

  <section class="intro">
    <div class="intro-kicker">ON THE OTHER HAND, <strong>WE DENOUNCE</strong><br>WITH RIGHTEOUS INDIGNATION</div>
    <h2 class="intro-title">LOREM IPSUM</h2>
  </section>

  <section class="promise">
    <ul class="promise-list">
      <li>PERFECT</li>
      <li>PRIVATE</li>
      <li>GUARANTEED</li>
    </ul>
    <p class="promise-copy">"But I must explain to you how all this mistaken idea of denouncing pleasure<br>and praising pain was born and I will give you a complete account of<br>the system, and expound the actual teachings of the great explorer of the truth<br>the master-builder of human happiness.<br>No one rejects, dislikes, or avoids pleasure itself, because it is pleasure,<br>but because those who do not know how to pursue pleasure rationally encounter<br>consequences<br>the master-builder of human happiness.<br>No one rejects, dislikes, or avoids pleasure itself, because it is pleasure,<br>but because those who do not know how to pursue pleasure rationally encounter<br>consequences</p>
    <a class="outline-button read-more" href="#">Read more</a>
  </section>

  <section class="features">
    <h3 class="feature-title">LOREM IPSUS ILSUM</h3>
    <a class="outline-button discover" href="#">Discover</a>
    <h3 class="offer-title">LOREM IPSUS ILSUM</h3>
    <p class="offer-copy">No one rejects, dislikes, or avoids pleasure<br>itself, because it is pleasure,<br>but because those who do not know how<br>to pursue pleasure rationally encounter<br>consequences</p>
  </section>

  <footer>
    <div class="footer-brand">Coral Cove Massage</div>
    <div class="footer-col" style="left:166px">
      <h4>COMPANY</h4>
      <p>hello@coralcove.test</p>
      <p>addres, number</p>
      <p>356 - 0192837</p>
    </div>
    <div class="footer-col" style="left:270px">
      <h4>COMMUNITY</h4>
      <p>lorem</p><p>ipsus</p><p>ilsum</p>
    </div>
    <div class="footer-col" style="left:371px">
      <h4>USEFUL LINKS</h4>
      <p>lorem</p><p>ipsus</p><p>ilsum</p>
    </div>
    <div class="social" aria-label="Social links">
      <span style="left:614px"></span>
      <span style="left:653px"></span>
      <span style="left:692px"></span>
    </div>
  </footer>
</div>
</body>
</html>
```